Global Parking App needs sleek business cards developed

We need a business card design for a soon-to-be launched global parking app called Vantle(TM). We need a sleek business card which ties in with the brand and existing logo.

We would like to see a designs that use the colors black and white. The final design should communicate the idea of 'cool'+'attitude'.

Business Card should contain the following:

FRONT

1. Logo and Strapline

Vantle(TM)
Your private parking space

2. Contact details

Lewis Hartigan
Managing Director
Vantle Technologies Pty Ltd
M: (+61)(0)417382916
E: lewis@vantle.example
W: www.vantle.example

BACK

The future of parking has arrived...

Same-style icons in a line of

1. a car
2. a motorbike/scooter
3. a boat
4. helicopter

Try Vantle(TM) today > (App Store logos, see attached)

www.vantle.example

```html
<!DOCTYPE html>
<html lang="en">
<head>
<meta charset="utf-8">
<title>Vantle business card, back</title>
<link rel="stylesheet" href="https://fonts.googleapis.com/css2?family=Source+Sans+3:wght@400;600&display=swap">
<style>
  :root {
    --backdrop: #e9e9e9;
    --card: #ffffff;
    --lime: #bcd833;
    --lime-soft: #d9ea86;
    --ink: #111111;
    --paper: #ffffff;
  }
  * { box-sizing: border-box; margin: 0; padding: 0; }
  html, body {
    width: 1200px;
    height: 1200px;
    overflow: hidden;
    background: var(--backdrop);
    font-family: "Source Sans 3", "Myriad Pro", sans-serif;
  }
  .card-back {
    position: absolute;
    left: 100px;
    top: 310px;
    width: 1000px;
    height: 580px;
    background: var(--card);
    overflow: hidden;
    box-shadow: 0 6px 18px rgba(0,0,0,0.18);
  }
  .world-map {
    position: absolute;
    inset: 0;
    background: linear-gradient(160deg, var(--lime) 0%, var(--lime-soft) 55%, var(--card) 100%);
  }
  .headline {
    position: absolute;
    top: 190px;
    left: 0;
    width: 100%;
    text-align: center;
    padding-left: 60px;
    font-size: 38px;
    font-weight: 400;
    color: var(--ink);
    letter-spacing: 0.2px;
    white-space: nowrap;
  }
  .vehicle-icons {
    position: absolute;
    top: 255px;
    left: 170px;
    display: flex;
    gap: 40px;
    list-style: none;
  }
  .vehicle-icon {
    width: 110px;
    height: 110px;
    border-radius: 50%;
    background: var(--ink);
    display: flex;
    align-items: center;
    justify-content: center;
  }
  .vehicle-icon svg { width: 74px; height: 74px; }
  .side-tab {
    position: absolute;
    right: 0;
    top: 262px;
    width: 120px;
    height: 54px;
    background: var(--ink);
  }
  .call-to-action {
    position: absolute;
    left: 48px;
    top: 420px;
    font-size: 30px;
    font-weight: 400;
    color: var(--ink);
    white-space: nowrap;
  }
  .store-badges {
    position: absolute;
    left: 48px;
    top: 472px;
    display: flex;
    gap: 18px;
  }
  .store-badge {
    width: 200px;
    height: 62px;
    border-radius: 9px;
    background: var(--ink);
  }
</style>
</head>
<body>
  <section class="card-back">
    <div class="world-map" role="img" aria-label="Lime green world map spread across the card"></div>

    <h1 class="headline">The future of parking has arrived...</h1>

    <ul class="vehicle-icons">
      <li class="vehicle-icon" aria-label="Car">
        <svg viewBox="0 0 74 74" fill="var(--paper)">
          <path d="M14 44 L18 30 Q20 24 27 24 L47 24 Q54 24 56 30 L60 44 Q64 45 64 49 L64 54 L10 54 L10 49 Q10 45 14 44 Z"/>
          <rect x="22" y="28" width="13" height="12" fill="var(--ink)"/>
          <rect x="39" y="28" width="13" height="12" fill="var(--ink)"/>
          <circle cx="22" cy="55" r="6" stroke="var(--ink)" stroke-width="2"/>
          <circle cx="52" cy="55" r="6" stroke="var(--ink)" stroke-width="2"/>
        </svg>
      </li>
      <li class="vehicle-icon" aria-label="Motorbike">
        <svg viewBox="0 0 74 74" fill="none" stroke="var(--paper)" stroke-linecap="round" stroke-linejoin="round">
          <circle cx="17" cy="52" r="9" stroke-width="5"/>
          <circle cx="57" cy="52" r="9" stroke-width="5"/>
          <path d="M17 52 L27 42 L47 40 L57 52" stroke-width="4"/>
          <path d="M24 40 L50 36 L52 44 L30 47 Z" fill="var(--paper)" stroke-width="2"/>
          <path d="M48 38 L51 28 L57 28" stroke-width="4"/>
          <circle cx="40" cy="14" r="5" fill="var(--paper)" stroke="none"/>
          <path d="M38 21 L33 36" stroke-width="6"/>
          <path d="M37 24 L50 29" stroke-width="4"/>
          <path d="M33 36 L43 42 L41 49" stroke-width="4"/>
        </svg>
      </li>
      <li class="vehicle-icon" aria-label="Boat">
        <svg viewBox="0 0 74 74" fill="var(--paper)">
          <path d="M26 14 L48 14 L50 30 L24 30 Z"/>
          <rect x="30" y="19" width="14" height="5" fill="var(--ink)"/>
          <path d="M14 32 L60 32 L54 52 L20 52 Z"/>
          <path d="M12 58 Q18 54 24 58 T36 58 T48 58 T62 58" fill="none" stroke="var(--paper)" stroke-width="3"/>
        </svg>
      </li>
      <li class="vehicle-icon" aria-label="Helicopter">
        <svg viewBox="0 0 74 74" fill="var(--paper)">
          <rect x="12" y="20" width="50" height="3" rx="1.5"/>
          <rect x="35" y="22" width="4" height="8"/>
          <path d="M26 30 L46 30 Q54 30 54 40 Q54 48 44 48 L28 48 Q22 48 22 40 Z"/>
          <path d="M28 38 L8 34 L8 40 L28 42 Z"/>
          <rect x="26" y="52" width="26" height="3" rx="1.5"/>
          <rect x="31" y="47" width="3" height="6"/>
          <rect x="44" y="47" width="3" height="6"/>
        </svg>
      </li>
    </ul>

    <div class="side-tab"></div>

    <p class="call-to-action">Try Vantle(TM) today</p>

    <div class="store-badges">
      <div class="store-badge" role="img" aria-label="App store download badge"></div>
      <div class="store-badge" role="img" aria-label="App store download badge"></div>
    </div>
  </section>
</body>
</html>
```